Keystone Arc Mentoring

We would like to refresh the design of our current website. We want to make it cleaner, more open and more professional looking using simple page layouts and crisp fonts. The site should be lighter and be easy to navigate.

It is important that it be easy to add and change content.

The current site can be seen at www.keystonearcmentor.example

As part of this, we want our logo colors to be darker blue and green more professional than they are currently. The current logo is attached as you can see the colors are too "neon"

THIS IS A WEBSITE DESIGN REFRESH PROJECT

Target Market(s)

Executives

Industry/Entity Type

Cleaner

Font styles to use
Sans Serif

Colors
0355a3
cfdfed
9bcb3c

Requirements
Must have
• Ease of use, ease of adding content
Should not have
• No crazy colors, not too busy...

```html
<!DOCTYPE html>
<html lang="en">
<head>
<meta charset="utf-8">
<title>Keystone Arc Mentoring</title>
<link href="https://fonts.googleapis.com/css2?family=Nunito+Sans:wght@400;600;700&display=swap" rel="stylesheet">
<style>
:root{
  --blue:#0355a3;
  --blue-dark:#024a8f;
  --pale:#cfdfed;
  --green:#9bcb3c;
  --text:#555a60;
  --rule:#d6d6d6;
  --panel:#eeeeee;
}
*{margin:0;padding:0;box-sizing:border-box}
html,body{width:866px;height:1200px;overflow:hidden}
body{font-family:"Nunito Sans",sans-serif;color:var(--text);background:#fff;position:relative}
.side-glow{position:absolute;top:0;width:44px;height:360px;background:linear-gradient(180deg,var(--green) 0%,#c9e49a 60%,#fff 100%)}
.side-glow.left{left:0}.side-glow.right{right:0}
.abs{position:absolute}
.brand{left:53px;top:40px;font-size:15px;font-weight:600;color:var(--blue);display:flex;align-items:center;gap:6px}
.brand .dot{width:12px;height:12px;border-radius:50%;background:var(--green)}
.connect{right:53px;top:29px;display:flex;align-items:center;gap:5px;font-size:12px;color:#555}
.connect .soc{width:20px;height:20px;border-radius:50%;background:var(--blue)}
.connect .soc:nth-child(3){background:#1a8fd6}
.connect .soc:nth-child(4){background:#2a7fb8}
.nav{left:53px;top:77px;width:760px;height:29px;background:var(--blue);display:flex;font-size:10.5px}
.nav a{color:#fff;text-decoration:none;display:flex;align-items:center;justify-content:center;flex:auto}
.nav a.active{background:var(--green);color:#1d3b5c;flex:0 0 78px}
.hero{left:53px;top:111px;width:760px;height:294px;border:2px solid #ddd;background:linear-gradient(100deg,#b9a48c 0%,#d9dde2 30%,#c7d3df 55%,#8d96a2 75%,#eef2f5 100%)}
.hero-title{left:80px;top:228px;font-size:47px;font-weight:600;color:var(--green);letter-spacing:-1px}
.dots{left:403px;top:376px;display:flex;gap:6px}
.dots i{width:10px;height:10px;border-radius:50%;background:#fff;display:block}
.dots i:first-child{background:var(--blue)}
h2{font-weight:400;color:var(--blue);font-size:17.5px}
.body-text{font-size:8.6px;line-height:15.4px;color:var(--text)}
.btn{display:inline-block;font-size:8.6px;color:#fff;background:var(--green);padding:8px 19px;letter-spacing:.3px}
.btn.blue{background:var(--blue)}
.rule{left:53px;top:591px;width:566px;height:1px;background:var(--rule)}
.service{width:164px}
.service .pic{height:102px;border:1px solid #ccc}
.service h3{font-weight:400;color:var(--blue);font-size:12.5px;margin-top:7px}
.service p{font-size:8.6px;line-height:13.5px;margin-top:3px;height:42px}
.service .more{font-size:7.6px;color:var(--blue);font-weight:700;margin-top:6px;display:block}
.resources{left:638px;top:431px;width:175px;height:198px;background:var(--blue);padding:12px 13px;color:#fff}
.resources h2{color:var(--green)}
.resources p{font-size:8.6px;line-height:15.4px;margin:7px 0 12px}
.ask{left:638px;top:638px;width:175px;height:227px;background:var(--panel);border:1px solid #ccc;padding:10px 11px}
.ask p{font-size:8.6px;line-height:13.5px;color:#444;padding:6px 0 5px;border-bottom:1px solid #ccc}
.ask p:last-of-type{border:none}
.band{left:0;top:885px;width:866px;height:188px;background:var(--green)}
.band h2{position:absolute;left:54px;top:19px}
.card{top:52px;width:239px;height:114px;background:#fff;padding:14px 14px;box-shadow:0 1px 3px rgba(0,0,0,.2)}
.card p{font-size:8.6px;line-height:15.4px;color:#555}
.card .q{color:var(--green);font-weight:700;font-size:18px;line-height:8px;vertical-align:-6px;margin-right:4px}
.card .who{color:var(--blue);font-size:8.6px;margin-top:3px}
.card .org{font-size:8.6px;color:#555}
.footer{left:0;top:1073px;width:866px;height:127px;background:linear-gradient(180deg,var(--pale) 0%,#fff 100%)}
.flinks{left:53px;top:22px;font-size:8.8px;color:#444}
.fbrand{left:53px;top:75px;font-size:11px;color:var(--blue);font-weight:600}
.copy{left:53px;top:95px;font-size:8.8px;color:#444}
.fcol{top:22px;font-size:8px;line-height:14px;color:#444}
.fcol h4{font-weight:400;font-size:10.5px;color:var(--blue);margin-bottom:1px}
</style>
</head>
<body>
<div class="side-glow left"></div>
<div class="side-glow right"></div>

<header>
  <div class="abs brand"><span class="dot"></span>Keystone Arc Mentoring</div>
  <div class="abs connect">Connect Us:<span class="soc"></span><span class="soc"></span><span class="soc"></span></div>
  <nav class="abs nav">
    <a class="active">Home</a><a>Why Coaching</a><a>About</a><a>Services</a><a>Clients</a><a>Resources</a><a>Blog</a><a>Testimonials</a><a>Contact</a>
  </nav>
</header>

<section>
  <div class="abs hero" role="img" aria-label="Photo of a business coach presenting at a whiteboard to two seated listeners in a bright office"></div>
  <div class="abs hero-title">FROM MY WAY.....</div>
  <div class="abs dots"><i></i><i></i><i></i><i></i></div>
</section>

<main>
  <div class="abs" style="left:54px;top:427px;width:566px">
    <h2>Welcome to Our Website</h2>
    <p class="body-text" style="margin-top:6px">Keystone Arc Mentoring works with executives and companies that are facing issues ranging from mild dysfunction to significant distress. We help them pivot, regain control and achieve renewed growth. Keystone Arc Mentoring employs the Core Momentum LeadershipTM process developed by Alan R. Whitfield PhD., founder of the Center for Applied Leadership Studies (CALS). Core Momentum LeadershipTM is the process that develops a personally effective style of leadership that positively influences and changes not only the leader, but also those with whom they work and interact, as well as their organization as a whole.</p>
    <span class="btn" style="margin-top:17px">READ MORE</span>
  </div>
  <div class="abs rule"></div>
  <div class="abs" style="left:54px;top:601px;width:566px">
    <h2>Our Services</h2>
    <p class="body-text" style="margin-top:3px">Keystone Arc Mentoring provides one-to-one and group coaching focused on enabling individuals and organizations to align their values, strengths and goals to achieve extraordinary, sustainable outcomes even in the most challenging situations.</p>
  </div>

  <div class="abs service" style="left:53px;top:672px">
    <div class="pic" role="img" aria-label="Photo of a smiling business team" style="background:linear-gradient(135deg,#e8eef2,#b99a7a)"></div>
    <h3>Leadership Coaching</h3>
    <p>The Stream of Consciousness, flows through only a few of the world's best organizations...</p>
    <span class="more">READ MORE ››</span>
  </div>
  <div class="abs service" style="left:248px;top:672px">
    <div class="pic" role="img" aria-label="Photo of a hand ticking checkboxes with a red pencil" style="background:linear-gradient(135deg,#f4f4f4,#e6c9b8)"></div>
    <h3>Assessments</h3>
    <p>Great coaching relationships start by meeting the client where<br>they are.</p>
    <span class="more">READ MORE ››</span>
  </div>
  <div class="abs service" style="left:443px;top:672px">
    <div class="pic" role="img" aria-label="Word cloud image about coaching and skills" style="background:linear-gradient(135deg,#2d5b6b,#8fb3bd)"></div>
    <h3>Skills Coaching</h3>
    <p>Most organizations invest in "training" their employees with the intention of increasing their productivity.</p>
    <span class="more">READ MORE ››</span>
  </div>

  <aside class="abs resources">
    <h2>Our Resources</h2>
    <p>All Keystone Arc Mentoring clients and prospective clients have access to a secure website of their own. The website enables us to record sessions, enter notes, set goals, schedule or re-schedule appointments and much more.</p>
    <span class="btn">READ MORE</span>
  </aside>
  <aside class="abs ask">
    <h2>Ask Your Self</h2>
    <p>Has my company lost it's momentum? Is it stuck in neutral or worse?</p>
    <p>Am I frustrated by the lack of cooperation and general apathy among my people?</p>
    <p>Is there a shared vision, do we have a true win-win culture?</p>
    <span class="btn blue" style="margin-top:22px">READ MORE</span>
  </aside>
</main>

<section class="abs band">
  <h2>Testimonials</h2>
  <div class="abs card" style="left:53px">
    <p><span class="q">&ldquo;</span>I've known Martin Hale, through business, for a number of years. I became a client of Keystone Arc Mentoring at the beginning of 2012 and it's easily one of the best decisions I made this year...</p>
    <div class="who">– Laura M., COO</div><div class="org">Harbor Events Group</div>
  </div>
  <div class="abs card" style="left:313px">
    <p><span class="q">&ldquo;</span>I've known Martin Hale, through business, for a number of years. I became a client of Keystone Arc Mentoring at the beginning of 2012 and it's easily one of the best decisions I made this year...</p>
    <div class="who">– Laura M., COO</div><div class="org">Harbor Events Group</div>
  </div>
  <div class="abs card" style="left:574px">
    <p><span class="q">&ldquo;</span>I've known Martin Hale, through business, for a number of years. I became a client of Keystone Arc Mentoring at the beginning of 2012 and it's easily one of the best decisions I made this year...</p>
    <div class="who">– Laura M., COO</div><div class="org">Harbor Events Group</div>
  </div>
</section>

<footer class="abs footer">
  <div class="abs flinks">Home &nbsp;/&nbsp; Why Coaching &nbsp;/&nbsp; About &nbsp;/&nbsp; Services &nbsp;/&nbsp; Clients &nbsp;/&nbsp; Resources &nbsp;/&nbsp; Blog / Testimonials &nbsp;/&nbsp; Contact</div>
  <div class="abs fbrand">Keystone Arc Mentoring</div>
  <div class="abs copy">Copyright © 2014 by Northgate Ridge, LLC.</div>
  <div class="abs fcol" style="left:573px">
    <h4>Contact Info</h4>210 Meadow Lane<br>Suite 4-B<br>Fairview, VA 20100
  </div>
  <div class="abs fcol" style="left:685px">
    <h4>Contact Us</h4>T: (555) 010-2040<br>F: (555) 010-2041<br>Email: info@keystonearcmentor.example
  </div>
</footer>
</body>
</html>
```